Groovy little Insurance brokerage needs a new look

We have a new logo, but need to work out how to make it work for us!
We are a small insurance broking firm (three staff with different focus and styles), with lots of energy, experience and enthusiasm. A focus on both commercial and domestic market. We would like our cards to show a fresh look - while veering away from the 'run of the mill' insurance industry (often dull) approach.
Updates

Thanks to all for your concepts.

Had some great ideas come back, now just the process of picking which one is going to work best for us...
Will advise when we've had an opportunity to review.

Thanks!
From the team at
Kestrel Dunmore Insurance Brokers

Thanks SO much to all of your for your great designs.  Now just a process of sorting out the favorites.  If yours is eliminated, just want to say a collective thank you for your efforts!

Industry/Entity Type

Business

```html
<!DOCTYPE html>
<html lang="en">
<head>
<meta charset="utf-8">
<title>Kestrel Dunmore Insurance Brokers – Business Card</title>
<link rel="stylesheet" href="https://fonts.googleapis.com/css2?family=Open+Sans:wght@400;600;700&family=Questrial&display=swap">
<style>
  :root {
    --sky: #8fcbdb;
    --teal: #2fb0cc;
    --ink: #262626;
    --paper: #ffffff;
    --backdrop: #2b2b2b;
    --row-dark: #555658;
    --row-mid: #6b6c6e;
    --band-grey: #a9aaac;
    --band-grey-light: #c2c3c5;
    --icon-grey: #8a8b8d;
  }
  * { margin: 0; padding: 0; box-sizing: border-box; }
  html, body {
    width: 1200px; height: 800px; overflow: hidden;
    background: var(--backdrop);
  }
  .business-card {
    position: absolute; left: 120px; top: 126px;
    width: 960px; height: 548px;
    background: var(--paper);
    overflow: hidden;
    font-family: "Open Sans", Arial, sans-serif;
  }
  .top-band {
    position: absolute; left: 0; top: 0; width: 100%; height: 82px;
    background: var(--sky);
  }
  .bottom-band {
    position: absolute; left: 0; top: 432px; width: 100%; height: 116px;
    background: linear-gradient(var(--band-grey) 0 62%, var(--paper) 62% 65%, var(--band-grey-light) 65% 100%);
  }
  .contact-list {
    position: absolute; left: 0; top: 150px; width: 345px;
    list-style: none;
  }
  .contact-item {
    display: flex; align-items: center;
    height: 46px; margin-bottom: 2px;
    padding-left: 128px;
    background: var(--row-dark);
    color: var(--paper);
    font-size: 17px;
    white-space: nowrap;
  }
  .contact-item:nth-child(even) { background: var(--row-mid); }
  .contact-icon {
    width: 30px; height: 30px; margin-right: 10px;
    display: flex; align-items: center; justify-content: center;
    background: var(--icon-grey);
    flex: none;
  }
  .contact-icon--social { background: var(--teal); }
  .contact-icon svg { width: 20px; height: 20px; }
  .brand-square {
    position: absolute; left: 360px; top: 150px;
    width: 150px; height: 150px;
    background: var(--teal);
  }
  .brand-name {
    position: absolute; left: 530px; top: 146px;
    font-family: "Open Sans", Arial, sans-serif;
    font-weight: 700; font-size: 140px; line-height: 1;
    color: var(--ink); letter-spacing: -2px;
    white-space: nowrap;
  }
  .brand-tagline {
    position: absolute; left: 534px; top: 292px;
    font-family: "Open Sans", Arial, sans-serif;
    font-weight: 700; font-size: 14.5px; letter-spacing: 1.6px;
    color: var(--teal); text-transform: uppercase;
    white-space: nowrap;
  }
  .person {
    position: absolute; right: 90px; top: 322px;
    text-align: left;
    font-family: "Questrial", "Century Gothic", sans-serif;
    color: var(--ink);
    white-space: nowrap;
  }
  .person-name { font-size: 42px; line-height: 1; letter-spacing: -1px; }
  .person-name .surname { color: var(--teal); font-weight: 700; }
  .person-role { font-size: 22px; line-height: 1.2; margin-top: 2px; letter-spacing: -0.5px; }
</style>
</head>
<body>
  <main class="business-card">
    <div class="top-band"></div>
    <div class="bottom-band"></div>

    <ul class="contact-list">
      <li class="contact-item">
        <span class="contact-icon">
          <svg viewBox="0 0 24 24" fill="#fff"><path d="M6.6 10.8a15.1 15.1 0 0 0 6.6 6.6l2.2-2.2a1 1 0 0 1 1-.25 11.4 11.4 0 0 0 3.6.57 1 1 0 0 1 1 1V20a1 1 0 0 1-1 1A17 17 0 0 1 3 4a1 1 0 0 1 1-1h3.5a1 1 0 0 1 1 1c0 1.25.2 2.45.57 3.57a1 1 0 0 1-.25 1z"/></svg>
        </span>000.000.0000
      </li>
      <li class="contact-item">
        <span class="contact-icon">
          <svg viewBox="0 0 24 24" fill="none" stroke="#fff" stroke-width="2"><rect x="3" y="6" width="18" height="12"/><path d="M3 6l9 7 9-7"/></svg>
        </span>info@you.com
      </li>
      <li class="contact-item">
        <span class="contact-icon">
          <svg viewBox="0 0 24 24" fill="none" stroke="#fff" stroke-width="1.6"><circle cx="12" cy="12" r="9"/><ellipse cx="12" cy="12" rx="4" ry="9"/><path d="M3 12h18M5 7h14M5 17h14"/></svg>
        </span>www.website.com
      </li>
      <li class="contact-item">
        <span class="contact-icon contact-icon--social"></span>facelink.net/you
      </li>
      <li class="contact-item">
        <span class="contact-icon contact-icon--social"></span>chirper.net/you
      </li>
      <li class="contact-item">
        <span class="contact-icon contact-icon--social"></span>workline.net/you
      </li>
    </ul>

    <div class="brand-square"></div>
    <div class="brand-name">kdib</div>
    <div class="brand-tagline">Kestrel Dunmore Insurance Brokers</div>

    <div class="person">
      <div class="person-name">JOHN<span class="surname">DOE</span></div>
      <div class="person-role">JOB POSITION</div>
    </div>
  </main>
</body>
</html>
```